Harrowgate Home Works Sales Flyer

We want a sales flyer that outlines our companies strengths with Kitchen & Bath Remodeling. We would like highlight those aspects while also showcasing our ability to do decks and home additions. We want financing packages to be a big part of the flyer.

Target Market(s)

Residential Customers

Requirements
Must have
• Financing options
Highlight Kitchen & bath remodeling
Less subtle is our decks and home additions
Nice to have
• Keep within our logo colors-we are looking for informative flyers that leave homeowners eager to call us after a meeting

```html
<!DOCTYPE html>
<html lang="en">
<head>
<meta charset="utf-8">
<title>Harrowgate Home Works – Sales Flyer</title>
<link rel="stylesheet" href="https://fonts.googleapis.com/css2?family=Oswald:wght@400;600;700&family=Montserrat:wght@400;500;600&display=swap">
<style>
  :root {
    --orange: #ef4a1c;
    --navy: #141c2e;
    --white: #ffffff;
    --ink: #1b2233;
    --cream: #fbe3d8;
    --photo-a: #d9d3cc;
    --photo-b: #a89f96;
  }
  * { margin: 0; padding: 0; box-sizing: border-box; }
  html, body { width: 1200px; height: 862px; overflow: hidden; background: #e9e6e2; }
  .flyer {
    position: relative; width: 1200px; height: 862px; overflow: hidden;
    background: var(--orange); font-family: "Montserrat", sans-serif; color: var(--white);
  }
  .masthead {
    position: absolute; left: 0; top: 0; width: 100%; height: 140px; background: var(--white);
    display: flex; align-items: center; padding: 0 48px;
  }
  .brand { display: flex; align-items: center; gap: 12px; width: 270px; }
  .brand-mark { width: 18px; height: 18px; background: var(--orange); }
  .brand-name { font-family: "Montserrat", sans-serif; font-weight: 600; font-size: 21px; line-height: 1.15; color: var(--orange); text-transform: uppercase; }
  .divider-v { width: 3px; height: 70px; background: var(--orange); margin: 0 34px; }
  .slogan { font-family: "Oswald", sans-serif; font-weight: 700; color: var(--ink); text-transform: uppercase; letter-spacing: 2px; line-height: 1.15; }
  .slogan-main { font-size: 30px; width: 330px; }
  .slogan-local .big { font-size: 32px; display: block; }
  .slogan-local .small { font-size: 18px; display: block; letter-spacing: 2.5px; }

  .rule { position: absolute; left: 0; width: 100%; height: 5px; background: var(--orange); }
  .photo-strip {
    position: absolute; left: 0; top: 150px; width: 100%; height: 182px;
    background: linear-gradient(90deg, var(--photo-a), var(--photo-b) 45%, var(--photo-a) 70%, #c4b6aa);
  }

  .headline-panel { position: absolute; left: 0; top: 337px; }
  .headline {
    position: absolute; left: 48px; top: 352px; font-family: "Oswald", sans-serif; text-transform: uppercase;
  }
  .headline .primary { font-size: 66px; font-weight: 700; color: var(--orange); letter-spacing: 3px; line-height: 1; display: block; }
  .headline .secondary { font-size: 26px; font-weight: 400; color: var(--ink); letter-spacing: 3px; display: block; margin-top: 4px; }

  .intro {
    position: absolute; left: 610px; top: 368px; padding-left: 24px; border-left: 2px solid var(--white);
    font-size: 16px; line-height: 1.6;
  }
  .intro .caps { text-transform: uppercase; letter-spacing: 1px; font-size: 15px; }

  .packages { position: absolute; left: 0; top: 500px; width: 100%; height: 210px; display: flex; padding: 0 48px; }
  .package { flex: 1; padding: 10px 40px; }
  .package + .package { border-left: 1px solid var(--cream); }
  .package h3 { font-family: "Oswald", sans-serif; font-weight: 400; font-size: 30px; letter-spacing: 3px; text-transform: uppercase; }
  .package p { font-size: 15px; line-height: 1.6; color: var(--cream); margin-top: 12px; }
  .package .price { font-family: "Oswald", sans-serif; font-weight: 700; font-size: 28px; letter-spacing: 3px; margin-top: 26px; padding-left: 50px; }

  .footer {
    position: absolute; left: 0; bottom: 0; width: 100%; height: 130px; background: var(--navy);
    display: flex; align-items: center; justify-content: space-between; padding: 0 48px;
  }
  .footer-info { color: var(--orange); font-size: 17px; line-height: 1.55; font-weight: 500; }
  .footer-info .company { text-transform: uppercase; }
  .footer-phone { display: flex; align-items: center; gap: 30px; }
  .footer-phone .sep { width: 2px; height: 70px; background: var(--orange); }
  .footer-phone .number { font-family: "Oswald", sans-serif; font-weight: 700; font-size: 68px; color: var(--orange); letter-spacing: 3px; }
</style>
</head>
<body>
<main class="flyer">
  <header class="masthead">
    <div class="brand">
      <span class="brand-mark"></span>
      <span class="brand-name">Harrowgate<br>Home Works</span>
    </div>
    <span class="divider-v"></span>
    <div class="slogan slogan-main">Refresh, Revitalise and Rejuvenate</div>
    <span class="divider-v"></span>
    <div class="slogan slogan-local">
      <span class="big">Your Home With Us</span>
      <span class="small">We Are Local, Just Like You</span>
    </div>
  </header>

  <div class="rule" style="top:140px"></div>
  <div class="photo-strip" role="img" aria-label="Photo collage of a remodeled white kitchen with range hood and a marble-tiled bathroom with glass shower"></div>
  <div class="rule" style="top:332px"></div>

  <svg class="headline-panel" width="620" height="140" viewBox="0 0 620 140" aria-hidden="true">
    <polygon points="0,0 590,0 540,140 0,140" fill="#ffffff"/>
  </svg>
  <h1 class="headline">
    <span class="primary">Kitchen &amp; Bath</span>
    <span class="secondary">+Decks and Home Additions</span>
  </h1>

  <div class="intro">
    <div>Transform Your Home With Superior Remodeling Services</div>
    <div class="caps">Hire a Premier Local Remodeling Company in Maple Ridge, IA</div>
  </div>

  <section class="packages">
    <article class="package">
      <h3>Package 1</h3>
      <p>Package Descriptions<br>Package Descriptions</p>
      <div class="price">Price $$$</div>
    </article>
    <article class="package">
      <h3>Package 2</h3>
      <p>Package Descriptions<br>Package Descriptions</p>
      <div class="price">Price $$$</div>
    </article>
    <article class="package">
      <h3>Package 3</h3>
      <p>Package Descriptions<br>Package Descriptions</p>
      <div class="price">Price $$$</div>
    </article>
  </section>

  <footer class="footer">
    <div class="footer-info">
      <div><span class="company">Harrowgate Home Works, LLC</span> | www.harrowgatehomeworks.com</div>
      <div>218 Birchline Avenue, Suite 4, Maple Ridge, IA 50099</div>
    </div>
    <div class="footer-phone">
      <span class="sep"></span>
      <span class="number">515-555-0148</span>
    </div>
  </footer>
</main>
</body>
</html>
```